Still Brook Trail - Business Card

May try various combos of colors from primary & secondary palette attached below. Logo and Catch phrase previous built logo attached should go on front, but change to color palette options noted. may try various color options from minimal to zen like quality/vibe.
On Front: Attached Logo & Phrase
On Back:
https://stillbrooktrail.com/
415.283.7904
stillbrooktrail@openlanterndesk.ai

Contact Information for Business Card

Daniel R. Forsyth, MD Founder & CEO https://stillbrooktrail.com/ 415.283.7904 stillbrooktrail@openlanterndesk.ai

```html
<!DOCTYPE html>
<html lang="en">
<head>
<meta charset="utf-8">
<title>Still Brook Trail – Business Card</title>
<link rel="stylesheet" href="https://fonts.googleapis.com/css2?family=Montserrat:wght@400;500;600&display=swap">
<style>
  :root {
    --forest: #435724;
    --peach: #edc199;
    --paper: #ffffff;
    --mist: #a3a39d;
    --stage: #e9e8e4;
  }
  * { box-sizing: border-box; margin: 0; padding: 0; }
  html, body { width: 1200px; height: 1200px; overflow: hidden; }
  body {
    background: var(--stage);
    font-family: "Montserrat", sans-serif;
    display: flex;
    flex-direction: column;
    align-items: center;
    justify-content: center;
    gap: 54px;
  }
  .card {
    position: relative;
    width: 880px;
    height: 503px;
    border-radius: 40px;
    overflow: hidden;
  }
  .card--contact { background: var(--paper); }
  .card--brand { background: var(--forest); }

  .contact-shape { position: absolute; inset: 0; width: 100%; height: 100%; }

  .contact-info {
    position: absolute;
    left: 78px;
    top: 175px;
    color: var(--paper);
  }
  .contact-name {
    font-size: 44px;
    font-weight: 600;
    color: var(--peach);
    letter-spacing: 1px;
    line-height: 1;
  }
  .contact-title {
    font-size: 22px;
    font-weight: 500;
    margin: 6px 0 28px 4px;
    letter-spacing: 0.5px;
  }
  .contact-list { list-style: none; }
  .contact-list li {
    display: flex;
    align-items: center;
    gap: 12px;
    font-size: 17px;
    line-height: 1;
    margin-bottom: 16px;
  }
  .contact-list svg { width: 20px; height: 20px; flex: none; }

  .mark {
    position: absolute;
    display: flex;
    align-items: center;
    gap: 14px;
  }
  .mark-dot {
    border-radius: 50%;
    flex: none;
  }
  .mark-name {
    font-weight: 500;
    white-space: nowrap;
  }
  .card--contact .mark {
    right: 60px;
    top: 120px;
    flex-direction: column;
  }
  .card--contact .mark-dot {
    width: 170px; height: 170px;
    border: 3px solid var(--forest);
  }
  .card--contact .mark-name { color: var(--forest); font-size: 24px; }

  .card--brand .mark {
    left: 50%;
    top: 52px;
    transform: translateX(-50%);
    flex-direction: column;
    gap: 24px;
  }
  .card--brand .mark-dot {
    width: 180px; height: 180px;
    border: 3px solid var(--peach);
  }
  .card--brand .mark-name { color: var(--peach); font-size: 58px; line-height: 1.1; }
  .tagline {
    position: absolute;
    left: 0; right: 0;
    top: 340px;
    text-align: center;
    color: var(--mist);
    font-size: 24px;
    letter-spacing: 0.5px;
  }
</style>
</head>
<body>

  <section class="card card--contact">
    <svg class="contact-shape" viewBox="0 0 880 503" preserveAspectRatio="none" aria-hidden="true">
      <path d="M300 0 Q570 190 555 503 H530 Q545 200 280 0 Z" fill="var(--peach)"/>
      <path d="M0 0 H276 Q541 200 524 503 H0 Z" fill="var(--forest)"/>
    </svg>
    <div class="contact-info">
      <h1 class="contact-name">FULL NAME</h1>
      <p class="contact-title">TITLE</p>
      <ul class="contact-list">
        <li>
          <svg viewBox="0 0 24 24" aria-hidden="true"><path fill="var(--peach)" d="M6.6 10.8a15 15 0 0 0 6.6 6.6l2.2-2.2c.3-.3.7-.4 1-.2 1.1.4 2.3.6 3.6.6.6 0 1 .4 1 1V20c0 .6-.4 1-1 1A17 17 0 0 1 3 4c0-.6.4-1 1-1h3.5c.6 0 1 .4 1 1 0 1.3.2 2.5.6 3.6.1.3 0 .7-.2 1z"/></svg>
          415.283.7904
        </li>
        <li>
          <svg viewBox="0 0 24 24" aria-hidden="true"><rect x="2" y="5" width="20" height="14" fill="var(--peach)"/><path d="M2 5l10 8 10-8" fill="none" stroke="var(--forest)" stroke-width="1.6"/></svg>
          stillbrooktrail@openlanterndesk.ai
        </li>
        <li>
          <svg viewBox="0 0 24 24" aria-hidden="true"><g fill="none" stroke="var(--peach)" stroke-width="1.6"><circle cx="12" cy="12" r="9.5"/><ellipse cx="12" cy="12" rx="4" ry="9.5"/><path d="M2.5 12h19M4 7h16M4 17h16"/></g></svg>
          stillbrooktrail.com
        </li>
      </ul>
    </div>
    <div class="mark">
      <span class="mark-dot"></span>
      <span class="mark-name">Still Brook Trail</span>
    </div>
  </section>

  <section class="card card--brand">
    <div class="mark">
      <span class="mark-dot"></span>
      <span class="mark-name">Still Brook Trail</span>
    </div>
    <p class="tagline">Nurturing Quiet Hearts, Habits &amp; Homes</p>
  </section>

</body>
</html>
```